ReelVows Identity
Pamphlet/Business Cards
@PH - please check your private message on top right once you login to your pixelhive account & reply.
Thanks
Hi, I like the card on top, but please don't include my contact info...
It should include things like "Toronto, Montreal, Ottawa, Vancouver, Calgary, Edmonton", website reelvows.ca, phone 1.877.555.0148, email info@reelvows-example.ca and facebook www.facebook.com/reelvows
We need a business card and 4x6 pamphlet designs, styled similar to our website http://reelvows-example.ca

```html
<!DOCTYPE html>
<html lang="en">
<head>
<meta charset="utf-8">
<title>ReelVows Identity – Pamphlets and Business Cards</title>
<link href="https://fonts.googleapis.com/css2?family=Open+Sans:ital,wght@0,400;0,600;0,700;1,700&display=swap" rel="stylesheet">
<style>
:root{
  --stage:#e9e6e1;
  --black:#0b0b0b;
  --charcoal:#1c1c1e;
  --panel:#2a2a2d;
  --silver:#c9cacd;
  --silver-light:#f1f1f2;
  --red:#d3121c;
  --red-dark:#8f0a10;
  --white:#ffffff;
  --muted:#bdbdbd;
}
*{box-sizing:border-box;margin:0;padding:0}
html,body{width:1200px;height:631px;overflow:hidden}
body{background:var(--stage);font-family:"Open Sans",Arial,sans-serif;position:relative}
.flyer{position:absolute;top:53px;width:470px;height:547px;background:var(--black);overflow:hidden;box-shadow:0 4px 14px rgba(0,0,0,.35)}
.flyer--front{left:48px}
.flyer--back{left:538px}
.flyer__header{position:absolute;left:0;top:0;width:100%;height:160px;background:radial-gradient(ellipse at 50% 0,#2c2c2c 0,var(--black) 70%)}
.brand{position:absolute;left:0;right:0;top:22px;display:flex;align-items:center;justify-content:center;gap:8px;color:var(--white);font-weight:700;font-size:22px;letter-spacing:1px}
.brand__dot{width:12px;height:12px;border-radius:50%;background:var(--silver)}
.headline{position:absolute;left:30px;top:88px;width:330px;font-style:italic;font-weight:700;font-size:20px;line-height:1.15;color:var(--white)}
.headline em{color:var(--red);font-style:italic}
.price-badge{position:absolute;right:34px;top:112px;width:96px;height:96px;border-radius:50%;background:radial-gradient(circle at 40% 35%,#ff3a3f,var(--red) 55%,var(--red-dark));border:3px solid var(--white);display:flex;align-items:center;justify-content:center;color:var(--white);font-weight:700;font-size:21px;z-index:3}
.swoosh{position:absolute;left:0;top:148px;width:100%;height:34px;z-index:2}
.photo{position:absolute;background:linear-gradient(180deg,#a9cbe6 0,#e4eef5 45%,#d8c3a1 70%,#b89c76 100%)}
.flyer--front .photo{left:0;top:168px;width:340px;height:300px}
.serves{position:absolute;right:0;width:130px;padding:18px 0 0 22px;background:linear-gradient(180deg,#303033,#18181a);color:var(--white)}
.flyer--front .serves{top:168px;height:300px;padding-top:120px}
.serves__title{font-weight:700;font-size:15px;letter-spacing:1px;margin-bottom:6px}
.serves__list{list-style:none;font-size:12px;line-height:1.5;color:var(--muted)}
.flyer__footer{position:absolute;left:0;bottom:0;width:100%;height:79px;background:var(--black);text-align:center}
.phone{font-weight:700;font-size:24px;color:var(--white);padding-top:12px}
.offer{font-style:italic;font-weight:700;font-size:15px;color:var(--red);margin-top:4px}
.packages{position:absolute;left:22px;top:180px;width:300px;color:var(--white)}
.packages h2{font-size:13px;font-weight:700;color:var(--red);margin:4px 0 3px}
.packages p{font-size:8px;color:var(--muted);margin-bottom:3px}
.packages ul{list-style:none;font-size:8px;line-height:1.55;color:var(--silver);margin-bottom:8px}
.packages li::before{content:"";display:inline-block;width:4px;height:4px;background:var(--red);margin-right:6px;vertical-align:middle}
.flyer--back .photo--side{left:345px;top:176px;width:112px;height:92px;background:linear-gradient(160deg,#3a2a2a,#8b6b60 55%,#f0e4dc)}
.flyer--back .photo--disc{left:28px;top:408px;width:52px;height:52px;border-radius:50%;background:radial-gradient(circle,#fff 0,#d6d6d6 40%,#6c6c6c 100%)}
.flyer--back .serves{top:282px;height:150px;width:112px;right:13px;padding-top:16px}
.flyer--back .flyer__footer{height:92px;text-align:left}
.flyer--back .offer{position:absolute;right:18px;top:6px;width:250px;text-align:left;font-size:13px;line-height:1.2}
.contacts{position:absolute;right:18px;top:46px;width:250px;font-size:9px;line-height:1.5;color:var(--white)}
.contacts strong{font-size:12px}
.website{position:absolute;left:22px;bottom:12px;font-weight:700;font-size:14px;color:var(--white)}
.card{position:absolute;left:1022px;width:168px;height:206px;box-shadow:0 4px 12px rgba(0,0,0,.35);overflow:hidden}
.card--contact{top:156px;background:linear-gradient(100deg,var(--white) 0,var(--silver-light) 45%,var(--silver) 100%)}
.card--brand{top:384px;background:linear-gradient(135deg,#fff 0,#d9d9dc 50%,#a9aaae 100%)}
.card .brand{position:absolute;color:var(--charcoal);font-size:14px;gap:6px}
.card--contact .brand{left:12px;right:auto;top:90px}
.card--brand .brand{top:60px}
.card .brand__dot{width:9px;height:9px;background:var(--charcoal)}
.card__details{position:absolute;left:12px;top:22px;font-size:7px;line-height:1.55;color:var(--charcoal)}
.card__cities{position:absolute;right:12px;top:20px;list-style:none;text-align:right;font-style:italic;font-weight:700;font-size:12px;line-height:1.35;color:var(--charcoal)}
.card__cities li:nth-child(even){font-size:9px;color:#666}
.card__swoosh{position:absolute;left:0;width:100%;height:40px}
.card__url{position:absolute;right:12px;bottom:16px;font-size:8px;color:var(--charcoal)}
</style>
</head>
<body>

<section class="flyer flyer--front">
  <div class="flyer__header">
    <div class="brand"><span class="brand__dot"></span>ReelVows</div>
    <h1 class="headline">Videography + <em>Photography</em><br>packages starting</h1>
  </div>
  <div class="price-badge">$1,995</div>
  <svg class="swoosh" viewBox="0 0 470 34" preserveAspectRatio="none" aria-hidden="true">
    <path d="M0 20 C120 0 300 34 470 8 L470 20 C300 34 120 10 0 30 Z" fill="#d9dadd"/>
    <path d="M0 14 C140 -2 300 26 470 2" stroke="#ffffff" stroke-width="2" fill="none"/>
  </svg>
  <div class="photo" role="img" aria-label="Bride and groom embracing on a sunny beach"></div>
  <aside class="serves">
    <h3 class="serves__title">SERVES</h3>
    <ul class="serves__list"><li>Toronto</li><li>Montreal</li><li>Ottawa</li><li>Vancouver</li><li>Calgary</li><li>Edmonton</li></ul>
  </aside>
  <footer class="flyer__footer">
    <p class="phone">1.877.555.0148</p>
    <p class="offer">Book Videography and Photography together and get 10% off</p>
  </footer>
</section>

<section class="flyer flyer--back">
  <div class="flyer__header">
    <div class="brand"><span class="brand__dot"></span>ReelVows</div>
    <h1 class="headline">Videography + <em>Photography</em><br>packages starting</h1>
  </div>
  <div class="price-badge">$1,995</div>
  <svg class="swoosh" viewBox="0 0 470 34" preserveAspectRatio="none" aria-hidden="true">
    <path d="M0 20 C120 0 300 34 470 8 L470 20 C300 34 120 10 0 30 Z" fill="#d9dadd"/>
    <path d="M0 14 C140 -2 300 26 470 2" stroke="#ffffff" stroke-width="2" fill="none"/>
  </svg>
  <div class="packages">
    <h2>Wedding Videography Packages</h2>
    <p>All of our wedding videography packages include:</p>
    <ul>
      <li>Full day coverage from prep to reception</li>
      <li>Two cinematographers with HD cameras</li>
      <li>Highlight film set to your music</li>
      <li>Full ceremony and speeches edit</li>
      <li>Custom menu DVD with chapters</li>
      <li>Online preview of your wedding film</li>
      <li>Same day edit available on request</li>
    </ul>
    <h2>Wedding Photography Packages</h2>
    <p>All of our wedding photography packages include:</p>
    <ul style="margin-left:70px">
      <li>Unlimited edited digital images</li>
      <li>Engagement session before the big day</li>
      <li>Online gallery for family and friends</li>
      <li>Print release for all your photos</li>
      <li>Custom designed photo album</li>
    </ul>
  </div>
  <div class="photo photo--side" role="img" aria-label="Wedding couple portrait"></div>
  <div class="photo photo--disc" role="img" aria-label="Wedding film disc"></div>
  <aside class="serves">
    <h3 class="serves__title">SERVES</h3>
    <ul class="serves__list"><li>Toronto</li><li>Montreal</li><li>Ottawa</li><li>Vancouver</li><li>Calgary</li><li>Edmonton</li></ul>
  </aside>
  <footer class="flyer__footer">
    <p class="offer">Book Videography and Photography together and get 10% off</p>
    <p class="contacts">Call us at <strong>1.877.555.0148</strong><br>email at info@reelvows-example.ca<br>www.facebook.com/reelvows</p>
    <p class="website">www.reelvows.ca</p>
  </footer>
</section>

<article class="card card--contact">
  <p class="card__details">1.877.555.0148<br>info@reelvows-example.ca<br>www.reelvows.ca</p>
  <ul class="card__cities"><li>Toronto</li><li>Montreal</li><li>Ottawa</li><li>Vancouver</li><li>Calgary</li><li>Edmonton</li></ul>
  <div class="brand"><span class="brand__dot"></span>ReelVows</div>
  <svg class="card__swoosh" style="top:150px" viewBox="0 0 168 40" preserveAspectRatio="none" aria-hidden="true">
    <path d="M0 24 C50 6 110 36 168 12 L168 40 L0 40 Z" fill="#1c1c1e"/>
  </svg>
</article>

<article class="card card--brand">
  <div class="brand"><span class="brand__dot"></span>ReelVows</div>
  <svg class="card__swoosh" style="top:120px" viewBox="0 0 168 40" preserveAspectRatio="none" aria-hidden="true">
    <path d="M0 26 C50 8 110 34 168 10" stroke="#ffffff" stroke-width="3" fill="none"/>
  </svg>
  <p class="card__url">www.reelvows.ca</p>
</article>

</body>
</html>
```